Halvern Roofing & Waterproofing HOA & Commercial Roofing Specialists

FRONT COVER (Panel 1)
Halvern Roofing & Waterproofing
HOA & Commercial Roofing Specialists
Protecting Communities.
Preserving Property Value.
Delivering Long-Term Solutions.
📍 Serving Orange County & Surrounding Areas
INSIDE LEFT PANEL (Panel 2)
Who We Are
Halvern Roofing & Waterproofing is a trusted HOA and commercial roofing specialist serving Orange County and surrounding areas. We understand the unique needs of homeowner associations, property managers, and commercial properties—delivering reliable service, clear communication, and long-lasting results.
✔ HOA-Focused Expertise
✔ Licensed & Insured
✔ Emergency Response Available
✔ Quality Workmanship You Can Trust
INSIDE MIDDLE PANEL (Panel 3)
Roofing Services
HOA & Commercial Roofing
• Emergency roof tarping & repairs — Starting at $550
• Small & large roof repairs
• Chimney cap and spark arrestor repairs
• Preventative roof maintenance
• Roof cleaning
• Full roof replacement
We work on all roof types:
✔ Flat Roofs (Torch down, TPO, & PVC)
✔ Tile Roofs (Clay tiles, concrete tiles, and more)
✔ Shingle Roofs - KLT certified contractor
• Coating (silicone or acrylic)
No matter the size or system—we’ve got you covered.
INSIDE RIGHT PANEL (Panel 4)
Gutter Services
• Small & large gutter repairs
• Gutter cleaning & maintenance
• New gutter installation & replacement
Proper drainage protects your building—let us handle it.
BACK LEFT PANEL (Panel 5)
Deck/Balcony Waterproofing Services
• Balcony/deck maintenance
• Deck resurfacing
• Small & large deck repairs
• Full deck reconstruction
Specialized waterproofing solutions to keep decks safe, compliant, and durable.
BACK COVER (Panel 6)
Why Choose Halvern?
✔ HOA & Commercial Specialists
✔ Fully Licensed & Insured
✔ Reliable Scheduling
✔ Clear Communication
✔ Quality Materials & Craftsmanship
License Information:
C-39 Roofing Contractor
General B Contractor
License #4729351
📍 Office Location:
14 Dunmore Street, Suite K Irvine, CA 92604
📞 Contact us today for a consultation
949-555-0172 or rfp@halvernroofs.example
🌐 Serving Orange County & surrounding areas

```html
<!DOCTYPE html>
<html lang="en">
<head>
<meta charset="utf-8">
<title>Halvern Roofing &amp; Waterproofing — Trifold Brochure</title>
<link href="https://fonts.googleapis.com/css2?family=Montserrat:wght@400;500;600;700;800&display=swap" rel="stylesheet">
<style>
:root{
  --blue:#0a8fe0;
  --blue-deep:#0b5fa8;
  --blue-bright:#13a4f2;
  --ink:#0b0b0d;
  --ink-soft:#1c1d21;
  --white:#ffffff;
  --red:#e3131b;
  --backdrop:#a6a6a6;
  --sky-top:#9fcdf0;
  --sky-low:#eef6fc;
  --photo-wood:#b98d5f;
  --photo-roof:#8e4a3a;
}
*{box-sizing:border-box;margin:0;padding:0}
html,body{width:1200px;height:2771px;overflow:hidden}
body{background:var(--backdrop);font-family:'Montserrat',sans-serif;color:var(--white);position:relative}
.spread{position:absolute;left:101px;width:999px;height:773px;overflow:hidden;background:var(--white);box-shadow:0 10px 24px rgba(0,0,0,.35)}
.spread--outside{top:1021px}
.spread--inside{top:1861px}
.abs{position:absolute}
.photo{position:absolute}
.photo--wood{background:linear-gradient(135deg,#d8b485,var(--photo-wood) 60%,#7b5634)}
.photo--roof{background:linear-gradient(160deg,#8f6a55,var(--photo-roof) 55%,#5e2e24)}
.photo--gutter{background:linear-gradient(150deg,#c9cfcf,#8c8e86 60%,#5d5b4f)}
.photo--house{background:linear-gradient(180deg,#b8d7f0 0%,#e3e6ea 45%,#c9b69d 75%,#6f7a55 100%)}
.photo--worker{background:linear-gradient(160deg,#3d3f44,#2a2c30 40%,#b38b60 75%,#8c6a47)}
.sky{position:absolute;background:linear-gradient(180deg,var(--sky-top),var(--sky-low) 70%,var(--white))}
.black{position:absolute;background:linear-gradient(180deg,var(--ink-soft),var(--ink))}
.eyebrow{font-weight:800;font-size:17px;color:var(--ink);letter-spacing:.2px}
.eyebrow span,.accent{color:var(--blue)}
.tile{position:absolute;width:104px;height:104px;border-radius:6px;overflow:hidden}
.tile--blue{background:linear-gradient(160deg,var(--blue-bright),var(--blue-deep));font-weight:700;font-size:12.5px;line-height:1.12;padding:34px 12px 0}
.brand{position:absolute;text-align:center;color:var(--ink)}
.brand__name{font-weight:800;letter-spacing:1px;display:inline-flex;align-items:center;gap:6px}
.brand__mark{display:inline-block;background:var(--blue);border-radius:50%}
.brand__tag{font-weight:500;letter-spacing:.4px}
.center{text-align:center}
.label-blue{color:var(--blue-bright);font-weight:800;font-size:14px;line-height:1.1;letter-spacing:.3px}
.small{font-size:10px;font-weight:500}
.divider{position:absolute;height:1px;background:#5b5b5f}
.pill{position:absolute;border-radius:16px;background:linear-gradient(90deg,var(--blue-deep),var(--blue-bright));font-weight:600;color:var(--white);display:flex;align-items:center;white-space:nowrap}
.checklist{list-style:none;position:absolute}
.checklist li{position:relative;padding-left:15px;font-size:13px;line-height:20px}
.checklist li::before{content:"";position:absolute;left:0;top:5px;width:10px;height:10px;border-radius:50%;background:var(--blue-bright)}
.checklist li::after{content:"";position:absolute;left:3px;top:7px;width:4px;height:2px;border-left:1.5px solid #fff;border-bottom:1.5px solid #fff;transform:rotate(-45deg)}
.checklist--dark li{color:var(--ink)}
.checklist--tight li{font-size:12px;line-height:17px}
.checklist--tight li::before{top:4px}
.checklist--tight li::after{top:6px}
.checklist li.dot::after{display:none}
.checklist li.dot::before{width:6px;height:6px;top:6px;left:2px}
.tagline{position:absolute;font-weight:700;font-size:12.5px;line-height:1.2}
.tagline span{color:var(--blue-bright)}
.pro-icon{position:absolute;text-align:center;font-weight:600;font-size:11px;line-height:1.1;width:80px}
</style>
</head>
<body>

<!-- OUTSIDE SPREAD -->
<section class="spread spread--outside">
  <div class="sky" style="left:0;top:0;width:999px;height:430px"></div>

  <!-- back-left panel: deck services -->
  <h2 class="eyebrow abs" style="left:47px;top:42px">WHY <span>CHOOSE HALVERN?</span></h2>
  <div class="tile tile--blue" style="left:42px;top:79px">Balcony &amp;<br>deck<br>maintenance</div>
  <div class="tile photo--wood" style="left:148px;top:79px" role="img" aria-label="Worker maintaining a wooden balcony deck"></div>
  <div class="tile photo--wood" style="left:42px;top:187px" role="img" aria-label="Gloved hands nailing new deck boards"></div>
  <div class="tile tile--blue" style="left:148px;top:187px">Deck<br>resurfacing</div>
  <div class="tile tile--blue" style="left:42px;top:295px">Small &amp;<br>large deck<br>repairs</div>
  <div class="tile photo--wood" style="left:148px;top:295px" role="img" aria-label="Carpenter measuring deck planks"></div>

  <div class="abs" style="left:0;top:418px;width:333px;height:7px;background:var(--blue)"></div>
  <div class="black" style="left:0;top:425px;width:333px;height:348px"></div>
  <div class="photo photo--worker" style="left:0;top:445px;width:190px;height:328px" role="img" aria-label="Contractor kneeling on deck boards during reconstruction"></div>
  <div class="abs" style="left:170px;top:455px">
    <div style="color:var(--blue-bright);font-weight:800;font-size:26px;line-height:.95">FULL<br>DECK</div>
    <div style="font-weight:800;font-size:14px;margin-top:6px">RECONSTRUCTION</div>
  </div>
  <svg class="abs" style="left:245px;top:530px" width="20" height="60" viewBox="0 0 20 60" aria-hidden="true">
    <path d="M10 2 V56" fill="none" stroke="#13a4f2" stroke-width="2.2"/>
    <path d="M3 48 L10 57 L17 48" fill="none" stroke="#13a4f2" stroke-width="2.2"/>
  </svg>

  <!-- back cover: why choose + contact -->
  <svg class="abs" style="left:333px;top:262px" width="333" height="511" viewBox="0 0 333 511" aria-hidden="true">
    <defs><linearGradient id="blk" x1="0" y1="0" x2="0" y2="1"><stop offset="0" stop-color="#1c1d21"/><stop offset="1" stop-color="#0b0b0d"/></linearGradient></defs>
    <polygon points="0,511 0,68 167,0 333,68 333,511" fill="url(#blk)"/>
  </svg>
  <svg class="abs" style="left:372px;top:38px" width="256" height="322" viewBox="0 0 256 322" aria-hidden="true">
    <defs><linearGradient id="hex" x1="0" y1="0" x2="0" y2="1"><stop offset="0" stop-color="#13a4f2"/><stop offset="1" stop-color="#0b5fa8"/></linearGradient></defs>
    <polygon points="128,3 252,74 252,248 128,319 4,248 4,74" fill="#fff" stroke="#13a4f2" stroke-width="4"/>
    <polygon points="128,14 242,80 242,242 128,308 14,242 14,80" fill="url(#hex)"/>
  </svg>
  <h2 class="abs center" style="left:400px;top:90px;width:200px;font-weight:800;font-size:17px;line-height:1.05">WHY<br>CHOOSE HALVERN?</h2>
  <ul class="abs" style="left:402px;top:139px;width:200px;list-style:none">
    <li style="display:flex;align-items:center;gap:9px;height:30px;border-bottom:1px solid rgba(255,255,255,.35);font-size:10.5px;font-weight:500"><svg width="18" height="18" viewBox="0 0 18 18"><circle cx="9" cy="9" r="8" fill="#0b0b0d"/><path d="M5 9l3 3 5-6" stroke="#fff" stroke-width="1.6" fill="none"/></svg>HOA &amp; Commercial Specialists</li>
    <li style="display:flex;align-items:center;gap:9px;height:30px;border-bottom:1px solid rgba(255,255,255,.35);font-size:10.5px;font-weight:500"><svg width="18" height="18" viewBox="0 0 18 18"><circle cx="9" cy="9" r="8" fill="#0b0b0d"/><path d="M5 9l3 3 5-6" stroke="#fff" stroke-width="1.6" fill="none"/></svg>Fully Licensed &amp; Insured</li>
    <li style="display:flex;align-items:center;gap:9px;height:30px;border-bottom:1px solid rgba(255,255,255,.35);font-size:10.5px;font-weight:500"><svg width="18" height="18" viewBox="0 0 18 18"><circle cx="9" cy="9" r="8" fill="#0b0b0d"/><path d="M5 9l3 3 5-6" stroke="#fff" stroke-width="1.6" fill="none"/></svg>Reliable Scheduling</li>
    <li style="display:flex;align-items:center;gap:9px;height:30px;border-bottom:1px solid rgba(255,255,255,.35);font-size:10.5px;font-weight:500"><svg width="18" height="18" viewBox="0 0 18 18"><circle cx="9" cy="9" r="8" fill="#0b0b0d"/><path d="M5 9l3 3 5-6" stroke="#fff" stroke-width="1.6" fill="none"/></svg>Clear Communication</li>
    <li style="display:flex;align-items:center;gap:9px;height:34px;font-size:10.5px;font-weight:500;line-height:1.1"><svg width="18" height="18" viewBox="0 0 18 18"><circle cx="9" cy="9" r="8" fill="#0b0b0d"/><path d="M5 9l3 3 5-6" stroke="#fff" stroke-width="1.6" fill="none"/></svg>Quality Materials &amp;<br>Craftsmanship</li>
  </ul>

  <div class="brand" style="left:333px;top:376px;width:333px;color:#fff">
    <div class="brand__name" style="font-size:26px">HALVERN<span class="brand__mark" style="width:8px;height:8px"></span></div>
    <div class="brand__tag" style="font-size:8px">ROOFING &amp; WATERPROOFING</div>
  </div>
  <div class="abs center" style="left:333px;top:452px;width:333px">
    <div class="label-blue">LICENSE INFORMATION</div>
    <div style="font-weight:700;font-size:10px;line-height:1.2;margin-top:8px">C-39 Roofing Contractor<br>General B Contractor</div>
  </div>
  <div class="abs" style="left:424px;top:517px;width:152px;height:22px;border-radius:11px;background:#fff;display:flex;overflow:hidden;font-weight:700;font-size:11.5px">
    <span style="background:var(--blue);width:72px;display:flex;align-items:center;justify-content:center;border-radius:11px">License</span>
    <span style="color:var(--ink);flex:1;display:flex;align-items:center;justify-content:center">#4729351</span>
  </div>
  <div class="divider" style="left:400px;top:551px;width:200px"></div>
  <div class="abs center" style="left:333px;top:565px;width:333px">
    <div class="label-blue">OFFICE LOCATION</div>
    <div class="small" style="margin-top:4px">14 Dunmore Street, Suite K Irvine, CA 92604</div>
  </div>
  <div class="divider" style="left:400px;top:606px;width:200px"></div>
  <div class="abs center" style="left:333px;top:618px;width:333px">
    <div class="label-blue">CONTACT US TODAY<br>FOR A CONSULTATION</div>
    <svg style="display:block;margin:8px auto 0" width="10" height="10" viewBox="0 0 10 10" aria-hidden="true"><path d="M2 1l2 0 1 2-1 1c.6 1.2 1.4 2 2.6 2.6l1-1 2 1 0 2c-4.5 0-7.6-3.1-7.6-7.6z" fill="#13a4f2"/></svg>
    <div class="small" style="margin-top:2px">949-555-0172</div>
    <svg style="display:block;margin:8px auto 0" width="10" height="8" viewBox="0 0 10 8" aria-hidden="true"><rect x=".5" y=".5" width="9" height="7" fill="#13a4f2"/><path d="M.5 .5l4.5 4 4.5-4" stroke="#0b0b0d" fill="none"/></svg>
    <div class="small" style="margin-top:2px">rfp@halvernroofs.example</div>
    <div class="small" style="margin-top:12px">Serving Orange County &amp; surrounding areas</div>
  </div>

  <!-- front cover -->
  <div class="brand" style="left:666px;top:42px;width:333px">
    <div class="brand__name" style="font-size:40px">HALVERN<span class="brand__mark" style="width:11px;height:11px"></span></div>
    <div class="brand__tag" style="font-size:12px;margin-top:2px">ROOFING &amp; WATERPROOFING</div>
  </div>
  <div class="photo photo--house" style="left:666px;top:160px;width:333px;height:262px" role="img" aria-label="Modern two-storey house with new roof"></div>
  <div class="abs" style="left:666px;top:418px;width:333px;height:4px;background:var(--blue)"></div>
  <div class="black" style="left:666px;top:422px;width:333px;height:351px"></div>
  <svg class="abs" style="left:740px;top:350px" width="180" height="80" viewBox="0 0 180 80" aria-hidden="true">
    <polygon points="0,76 90,6 180,76 162,76 90,22 18,76" fill="#13a4f2"/>
    <polygon points="20,76 90,24 160,76" fill="#1c1d21"/>
    <rect x="84" y="52" width="5" height="5" fill="#fff"/><rect x="91" y="52" width="5" height="5" fill="#fff"/>
    <rect x="84" y="59" width="5" height="5" fill="#fff"/><rect x="91" y="59" width="5" height="5" fill="#fff"/>
  </svg>
  <h1 class="abs center" style="left:666px;top:452px;width:333px;font-weight:800;font-size:31px;line-height:1">HALVERN<br>ROOFING <span style="font-weight:500">&amp;</span><br><span style="color:var(--blue-bright)">WATERPROOFING</span></h1>
  <p class="abs center" style="left:666px;top:550px;width:333px;font-weight:700;font-size:12.5px;line-height:1.15">HOA &amp; Commercial Roofing<br>Specialists</p>
  <div class="pro-icon" style="left:767px;top:610px;transform:translateX(-50%)">
    <svg width="30" height="30" viewBox="0 0 30 30" aria-hidden="true"><circle cx="15" cy="15" r="11" fill="none" stroke="#13a4f2" stroke-width="1.6"/><path d="M15 8l6 3v5c0 4-3 6-6 7-3-1-6-3-6-7v-5z" fill="none" stroke="#13a4f2" stroke-width="1.6"/></svg>
    <div>Protecting<br>Communities</div>
  </div>
  <div class="abs" style="left:813px;top:605px;width:1px;height:72px;background:#55565b"></div>
  <div class="pro-icon" style="left:857px;top:610px;transform:translateX(-50%)">
    <svg width="30" height="30" viewBox="0 0 30 30" aria-hidden="true"><path d="M4 15L15 5l11 10M8 12v13h14V12" fill="none" stroke="#13a4f2" stroke-width="1.6"/><rect x="12" y="17" width="6" height="8" fill="none" stroke="#13a4f2" stroke-width="1.6"/></svg>
    <div>Preserving<br>Property<br>Value</div>
  </div>
  <div class="abs" style="left:900px;top:605px;width:1px;height:72px;background:#55565b"></div>
  <div class="pro-icon" style="left:946px;top:610px;transform:translateX(-50%)">
    <svg width="30" height="30" viewBox="0 0 30 30" aria-hidden="true"><circle cx="15" cy="11" r="6" fill="none" stroke="#13a4f2" stroke-width="1.6"/><path d="M5 24c3-3 6-4 10-4s7 1 10 4" fill="none" stroke="#13a4f2" stroke-width="1.6"/></svg>
    <div>Delivering<br>Long-Term<br>Solutions</div>
  </div>
  <svg class="abs" style="left:827px;top:704px" width="12" height="12" viewBox="0 0 12 12" aria-hidden="true"><circle cx="6" cy="6" r="6" fill="#13a4f2"/><path d="M6 2.5a2.2 2.2 0 0 0-2.2 2.2C3.8 6.5 6 9.5 6 9.5s2.2-3 2.2-4.8A2.2 2.2 0 0 0 6 2.5z" fill="#fff"/></svg>
  <div class="pill" style="left:708px;top:716px;width:250px;height:22px;font-size:10px;justify-content:center">Serving Orange County &amp; Surrounding Areas</div>
</section>

<!-- INSIDE SPREAD -->
<section class="spread spread--inside">
  <div class="sky" style="left:288px;top:0;width:711px;height:545px;background:linear-gradient(180deg,#ffffff 0%,#ffffff 40%,#cfe4f4 65%,#eef4f8 100%)"></div>
  <div class="photo photo--roof" style="left:288px;top:275px;width:711px;height:270px;background:linear-gradient(170deg,rgba(200,80,60,0) 0%,#a54a36 25%,#8e4a3a 60%,#6b3328 100%)" role="img" aria-label="Roofer working on a red tile roof"></div>

  <div class="black" style="left:0;top:544px;width:999px;height:229px"></div>
  <div class="abs" style="left:0;top:536px;width:999px;height:8px;background:var(--blue)"></div>
  <svg class="abs" style="left:735px;top:484px" width="190" height="62" viewBox="0 0 190 62" aria-hidden="true">
    <polygon points="0,60 95,4 190,60 170,60 95,20 20,60" fill="#13a4f2"/>
    <polygon points="22,62 95,22 168,62" fill="#1c1d21"/>
  </svg>

  <!-- inside left: who we are -->
  <svg class="abs" style="left:43px;top:42px" width="245" height="731" viewBox="0 0 245 731" aria-hidden="true">
    <polygon points="0,731 0,72 123,0 245,72 245,731" fill="#111114"/>
  </svg>
  <div class="photo" style="left:0;top:570px;width:288px;height:203px;background:linear-gradient(180deg,rgba(17,17,20,1) 0%,#6f5a48 45%,#3b3e45 80%,#1f2024 100%)" role="img" aria-label="Roofer standing on a metal roof ridge"></div>
  <h2 class="abs" style="left:80px;top:128px;font-weight:800;font-size:17px">WHO <span style="color:var(--blue-bright)">WE ARE</span></h2>
  <p class="abs" style="left:80px;top:166px;width:190px;font-size:13px;line-height:15.5px;font-weight:500">Halvern Roofing &amp; Waterproofing is a trusted HOA and commercial roofing specialist serving Orange County and surrounding areas. We understand the unique needs of homeowner associations, property managers, and commercial properties—delivering reliable service, clear communication, and long-lasting results.</p>
  <div class="pill" style="left:80px;top:408px;width:185px;height:32px;font-size:10.5px;padding-left:14px">HOA-Focused Expertise</div>
  <div class="pill" style="left:80px;top:447px;width:185px;height:32px;font-size:10.5px;padding-left:14px">Licensed &amp; Insured</div>
  <div class="pill" style="left:80px;top:486px;width:185px;height:32px;font-size:10.5px;padding-left:14px">Emergency Response Available</div>
  <div class="pill" style="left:80px;top:525px;width:185px;height:34px;font-size:10.5px;padding-left:14px;line-height:1.05;white-space:normal">Quality Workmanship You<br>Can Trust</div>

  <!-- inside middle: roofing services -->
  <h2 class="eyebrow abs" style="left:378px;top:42px">ROOFING <span>SERVICES</span></h2>
  <div class="pill" style="left:378px;top:71px;width:210px;height:24px;font-size:12.5px;padding-left:14px;background:linear-gradient(90deg,#0b5fa8,#0a8fe0)">HOA &amp; Commercial Roofing</div>
  <div class="abs" style="left:378px;top:108px;color:var(--ink);font-weight:600;font-size:12.5px;line-height:1.1">Emergency<br>roof tarping<br>&amp; repairs</div>
  <div class="abs" style="left:481px;top:104px;width:1px;height:56px;background:#b9b9b9"></div>
  <div class="abs" style="left:488px;top:106px;color:var(--ink);font-weight:600;font-size:12.5px">Starting at</div>
  <div class="abs" style="left:488px;top:120px;color:var(--red);font-weight:800;font-size:38px;line-height:1;display:flex;align-items:flex-start"><span style="font-size:18px;margin-right:2px;margin-top:2px">$</span>550</div>
  <div class="abs" style="left:378px;top:170px;width:210px;height:1px;background:#b9b9b9"></div>
  <ul class="checklist checklist--dark checklist--tight" style="left:378px;top:177px;width:300px">
    <li>Small &amp; large roof repairs</li>
    <li>Chimney cap &amp; spark arrestor repairs</li>
    <li>Preventative roof maintenance</li>
    <li>Roof cleaning</li>
    <li>Full roof replacement</li>
  </ul>

  <!-- inside right: photo grid -->
  <div class="tile photo--gutter" style="left:713px;top:44px;width:117px;height:117px;border-radius:8px" role="img" aria-label="Water flowing from a gutter downspout"></div>
  <div class="tile photo--gutter" style="left:836px;top:44px;width:117px;height:117px;border-radius:8px" role="img" aria-label="Gutter filled with debris"></div>
  <div class="tile photo--worker" style="left:713px;top:167px;width:117px;height:117px;border-radius:8px" role="img" aria-label="Worker in safety vest repairing a gutter"></div>
  <div class="tile" style="left:836px;top:167px;width:117px;height:117px;border-radius:8px;background:linear-gradient(160deg,#8fb0c8,#a2573f 50%,#3f5a32)" role="img" aria-label="Workers on a lift cleaning tile roof gutters"></div>

  <!-- bottom lists -->
  <div class="pill" style="left:378px;top:568px;width:210px;height:24px;font-size:12.5px;padding-left:14px">We work on all roof types</div>
  <ul class="checklist checklist--tight" style="left:378px;top:600px;width:320px">
    <li>Flat Roofs (Torch down, TPO, &amp; PVC)</li>
    <li>Tile Roofs (Clay tiles, concrete tiles, and more)</li>
    <li>Shingle Roofs – KLT certified contractor</li>
    <li class="dot">Coating (silicone or acrylic)</li>
  </ul>
  <p class="tagline" style="left:378px;top:686px;width:200px">No matter the size or system—<span>we’ve got you covered.</span></p>

  <div class="pill" style="left:711px;top:568px;width:210px;height:24px;font-size:12.5px;padding-left:14px">Gutter Services</div>
  <ul class="checklist" style="left:711px;top:600px">
    <li>Small &amp; large gutter repairs</li>
    <li>Gutter cleaning &amp; maintenance</li>
    <li style="line-height:15px;padding-top:2px">New gutter installation &amp;<br>replacement</li>
  </ul>
  <p class="tagline" style="left:711px;top:700px;width:220px">Proper drainage protects your building—<span>let us handle it.</span></p>
</section>

</body>
</html>
```